Website Design for Videographer

I am looking to update my website - www.lukebranwell.com. I am a wedding videographer who specialises in natural and documentary videography.

The website will be built by my designer using the Wordpress Brightform framework.

Requirements;
I want the website to have a clean white look mixed in with video footage.
Needs to be classy. At the moment my website uses a lot of Gold. On the new look I DO NOT want gold.

Need a web and mobile design for the following 12 pages;

* Home page (need to have example videos and text)
* About (this is about me and my service)
* Videos (examples of my work)
* Testimonials
* Packages
* Contact
* Content (this is to show social media content that I am making in a vertical format and advertise this service).
* Blog (index page for blog)
* Blog pages (individual pages for blog content)
* Wedding Venues Index Page (https://lukebranwell.com/north-east-wedding-venues/)
* Individual venue pages (https://lukebranwell.com/north-east-wedding-venues/holmfield-lodge-wedding-videos/) - Needs to show videos, photos, text as is on the current page.
* Venue Tours (https://lukebranwell.com/wedding-venue-tours/)

My current logo is attached however on the website I want to go for a black and white style for it.

Example styles I like however must not be copied.
https://joelmarrick.co.uk/about/
https://stoneandfern.co.uk/ (if done in white)
https://bouncyplumreels.co.uk/

Target Market(s)

Couples getting married aged 25-35

Industry/Entity Type

Weddings

Number of Pages Required

5+ page

Font styles to use
Sans Serif

Requirements
Must have
• A classy look, black and white, use videos and photos.
Should not have
• Gold colour

```html
<!DOCTYPE html>
<html lang="en">
<head>
<meta charset="utf-8">
<title>North East Wedding Videographer – Blog | Luke Branwell Wedding Films</title>
<link href="https://fonts.googleapis.com/css2?family=Cinzel:wght@400&family=Poppins:wght@300;400;500;600&display=swap" rel="stylesheet">
<style>
:root{
  --ink:#111111;
  --text:#222222;
  --muted:#555555;
  --soft:#8a8a8a;
  --paper:#ffffff;
  --mist:#f4f4f4;
  --card-active:#888888;
  --footer:#6b6b6b;
  --line:#d9d9d9;
}
*{box-sizing:border-box;margin:0;padding:0}
html,body{width:1200px;height:3525px;overflow:hidden;background:var(--paper)}
body{font-family:'Poppins',sans-serif;color:var(--text);position:relative}
a{color:inherit;text-decoration:none}

/* header */
.site-header{position:absolute;top:0;left:0;width:1200px;height:124px;background:var(--paper)}
.nav-link{position:absolute;top:54px;font-size:12px;letter-spacing:.2px;text-transform:uppercase;color:var(--ink)}
.brand{position:absolute;left:0;width:1200px;text-align:center;font-weight:500;letter-spacing:4px;text-transform:uppercase}
.site-header .brand{top:72px;font-size:18px;color:var(--ink)}
.btn-enquire{position:absolute;left:997px;top:34px;width:137px;height:45px;background:var(--ink);color:var(--paper);font-size:13px;font-weight:600;display:flex;align-items:center;justify-content:center;border-radius:2px}

/* hero */
.hero-intro{position:absolute;top:124px;left:0;width:1200px;height:345px;background:var(--mist)}
.hero-title{position:absolute;top:100px;width:1200px;text-align:center;font-family:'Cinzel',serif;font-weight:400;font-size:58px;line-height:63px;letter-spacing:3px;color:var(--ink)}
.btn-mark{position:absolute;left:472px;width:257px;height:61px;background:var(--ink);color:var(--paper);display:flex;align-items:center;font-size:17px;font-weight:500}
.btn-mark .mark{width:70px;height:61px;background:var(--paper);display:flex;align-items:center;justify-content:center}
.btn-mark .mark span{width:26px;height:26px;background:var(--ink)}
.btn-mark .label{flex:1;text-align:center;padding-right:10px}
.hero-intro .btn-mark{top:248px}
.hero-media{position:absolute;top:469px;left:0;width:1200px;height:643px;
  background:linear-gradient(180deg,#e9ebe8 0%,#a9b3a4 14%,#5f7a52 38%,#4a6136 62%,#3c4f28 100%)}

/* blog */
.blog-head{position:absolute;top:1208px;width:1200px;text-align:center}
.blog-title{font-family:'Cinzel',serif;font-weight:400;font-size:55px;letter-spacing:2px;color:var(--ink);line-height:68px}
.blog-title span{color:var(--soft)}
.blog-sub{margin-top:20px;font-size:31px;font-weight:500;color:var(--ink);letter-spacing:.3px}
.post-grid{position:absolute;top:1423px;left:68px;display:grid;grid-template-columns:repeat(3,327px);column-gap:42px;row-gap:30px}
.post-card{position:relative;width:327px;height:479px;background:var(--paper);box-shadow:0 0 8px rgba(0,0,0,.13);padding:5px}
.post-card.is-active{background:var(--card-active);color:var(--paper)}
.post-media{height:241px;position:relative}
.post-date{position:absolute;left:21px;top:40px;background:var(--paper);color:var(--ink);font-size:12.5px;height:38px;padding:0 18px;display:flex;align-items:center;gap:7px}
.post-body{padding:23px 21px 0 21px}
.post-title{font-size:20px;font-weight:400;line-height:27px;color:var(--ink)}
.is-active .post-title{color:var(--paper);text-decoration:underline;text-underline-offset:4px;text-decoration-thickness:1px}
.post-excerpt{margin-top:10px;font-size:12px;line-height:22.5px;color:var(--muted)}
.is-active .post-excerpt{color:var(--paper)}
.post-more{position:absolute;left:26px;top:420px;font-size:13px;font-weight:600;color:var(--ink);border-bottom:1px solid currentColor;line-height:17px}
.is-active .post-more{color:var(--paper)}
.load-more{top:2989px}

/* footer */
.site-footer{position:absolute;top:3166px;left:0;width:1200px;height:359px;background:var(--footer);color:var(--paper)}
.site-footer .brand{top:120px;font-size:19px;color:var(--paper)}
.footer-rule{position:absolute;top:135px;height:1px;background:#b5b5b5;width:379px}
.footer-nav .nav-link{color:var(--paper);top:222px}
.footer-enquire{position:absolute;left:525px;top:205px;width:137px;height:52px;border:1px solid var(--paper);display:flex;align-items:center;justify-content:center;font-size:14px;font-weight:500}
.footer-divider{position:absolute;left:68px;top:291px;width:1066px;height:1px;background:#8f8f8f}
.copyright{position:absolute;left:64px;top:311px;font-size:10.5px}
.social{position:absolute;top:300px;width:38px;height:38px;border-radius:50%;border:1.5px solid var(--paper)}
.social.filled{background:var(--paper)}
</style>
</head>
<body>

<header class="site-header">
  <a class="nav-link" href="#" style="left:69px">Home</a>
  <a class="nav-link" href="#" style="left:142px">About Luke</a>
  <a class="nav-link" href="#" style="left:264px">Wedding Films</a>
  <a class="nav-link" href="#" style="left:397px">Blog</a>
  <div class="brand">Luke Branwell</div>
  <a class="nav-link" href="#" style="left:770px">Testimonials</a>
  <a class="nav-link" href="#" style="left:889px">Packages</a>
  <a class="btn-enquire" href="#">ENQUIRE</a>
</header>

<section class="hero-intro">
  <h1 class="hero-title">North East Wedding<br>Videographer</h1>
  <a class="btn-mark" href="#"><span class="mark"><span></span></span><span class="label">BOOK WITH ME</span></a>
</section>
<div class="hero-media" role="img" aria-label="Wedding couple embracing beside a woodland lake surrounded by ferns and trees"></div>

<section class="blog-head">
  <h2 class="blog-title">Our <span>Blog</span></h2>
  <p class="blog-sub">FILMS, NEWS AND MEMORIES</p>
</section>

<svg width="0" height="0" style="position:absolute">
  <symbol id="icon-calendar" viewBox="0 0 12 12"><rect x="1" y="2" width="10" height="9" fill="none" stroke="currentColor" stroke-width="1.2"/><line x1="1" y1="5" x2="11" y2="5" stroke="currentColor" stroke-width="1.2"/><line x1="4" y1="0.5" x2="4" y2="3" stroke="currentColor" stroke-width="1.2"/><line x1="8" y1="0.5" x2="8" y2="3" stroke="currentColor" stroke-width="1.2"/></symbol>
</svg>

<section class="post-grid">
  <article class="post-card">
    <div class="post-media" role="img" aria-label="Best man laughing with the groom at a wedding reception" style="background:linear-gradient(135deg,#3c5a2e,#8a9a7a 55%,#3a4566)">
      <span class="post-date"><svg width="12" height="12"><use href="#icon-calendar"/></svg>Sept 9, 2024</span></div>
    <div class="post-body"><h3 class="post-title">What's the role of a best man at a wedding?</h3>
    <p class="post-excerpt">The best man ensures the wedding flows well and offers vital support to the groom...</p></div>
    <a class="post-more" href="#">READ MORE</a>
  </article>
  <article class="post-card is-active">
    <div class="post-media" role="img" aria-label="Bride and groom walking through guests in a woodland ceremony" style="background:linear-gradient(135deg,#2f4a25,#a08a6e 50%,#d8d3c8)">
      <span class="post-date"><svg width="12" height="12"><use href="#icon-calendar"/></svg>Sept 23, 2024</span></div>
    <div class="post-body"><h3 class="post-title">Larkmoor Tower – Nina and Tom</h3>
    <p class="post-excerpt">Love, laughter, and treasured memories abound in Nina and Tom's rustic woodland wedding held at...</p></div>
    <a class="post-more" href="#">READ MORE</a>
  </article>
  <article class="post-card">
    <div class="post-media" role="img" aria-label="Ivy-covered red brick country house wedding venue" style="background:linear-gradient(180deg,#b9c3cc,#7a4a3a 45%,#4d6a30 100%)">
      <span class="post-date"><svg width="12" height="12"><use href="#icon-calendar"/></svg>Sept 5, 2024</span></div>
    <div class="post-body"><h3 class="post-title">What Does It Mean to Have a Wedding Venue All to Yourself?</h3>
    <p class="post-excerpt">Exclusive use weddings are trending, offering unmatched privacy, personalization, and...</p></div>
    <a class="post-more" href="#">READ MORE</a>
  </article>

  <article class="post-card">
    <div class="post-media" role="img" aria-label="Aerial view of a barn wedding venue among trees" style="background:linear-gradient(135deg,#2f4a26,#6f7f5c 50%,#9a9a90)">
      <span class="post-date"><svg width="12" height="12"><use href="#icon-calendar"/></svg>Aug 12, 2024</span></div>
    <div class="post-body"><h3 class="post-title">10 Must-Ask Questions Before Booking Your Wedding Venue</h3>
    <p class="post-excerpt">Choosing a wedding venue is one of the most important decisions you will make during...</p></div>
    <a class="post-more" href="#">READ MORE</a>
  </article>
  <article class="post-card">
    <div class="post-media" role="img" aria-label="Printed save the date card on a grey textured surface" style="background:linear-gradient(135deg,#e2e3e3,#c9cbcc 60%,#9ea1a3)">
      <span class="post-date"><svg width="12" height="12"><use href="#icon-calendar"/></svg>Aug 5, 2024</span></div>
    <div class="post-body"><h3 class="post-title">When to Send Out “Save the Date” Cards?</h3>
    <p class="post-excerpt">Discover When To Send Out 'Save The Date' Cards For Your Wedding. Learn The Perfect...</p></div>
    <a class="post-more" href="#">READ MORE</a>
  </article>
  <article class="post-card">
    <div class="post-media" role="img" aria-label="Couple sharing their first dance surrounded by guests" style="background:linear-gradient(135deg,#3a2e2a,#8a6a5a 50%,#c8c0b8)">
      <span class="post-date"><svg width="12" height="12"><use href="#icon-calendar"/></svg>Jul 15, 2024</span></div>
    <div class="post-body"><h3 class="post-title">First Dance at Weddings</h3>
    <p class="post-excerpt" style="margin-top:22px">Exploring the first dance tradition at weddings, its significance, and how it creates a memorable...</p></div>
    <a class="post-more" href="#">READ MORE</a>
  </article>

  <article class="post-card">
    <div class="post-media" role="img" aria-label="Lakeside ceremony with bride under a floral arch" style="background:linear-gradient(135deg,#5f7fa0,#c9a48a 50%,#b44a3a)">
      <span class="post-date"><svg width="12" height="12"><use href="#icon-calendar"/></svg>Jul 8, 2024</span></div>
    <div class="post-body"><h3 class="post-title">Destination Wedding Videography</h3>
    <p class="post-excerpt">From choosing a location to coordinating travel arrangements for guests, there are many things to...</p></div>
    <a class="post-more" href="#">READ MORE</a>
  </article>
  <article class="post-card">
    <div class="post-media" role="img" aria-label="Couple exchanging vows in a stone chapel" style="background:linear-gradient(135deg,#d8cfc2,#b8a48c 55%,#5a4a3e)">
      <span class="post-date"><svg width="12" height="12"><use href="#icon-calendar"/></svg>Jun 27, 2024</span></div>
    <div class="post-body"><h3 class="post-title">Black-Tie Wedding at Ashcombe Park, Harrogate</h3>
    <p class="post-excerpt">Rosa and Dan celebrated a classy black-tie wedding at the stunning Ashcombe Park in Harrogate...</p></div>
    <a class="post-more" href="#">READ MORE</a>
  </article>
  <article class="post-card">
    <div class="post-media" role="img" aria-label="Newlyweds pouring a champagne tower in a garden" style="background:linear-gradient(135deg,#3f6a2e,#d9d9d4 55%,#2a2a2a)">
      <span class="post-date"><svg width="12" height="12"><use href="#icon-calendar"/></svg>Jun 25, 2024</span></div>
    <div class="post-body"><h3 class="post-title">Elegant Wedding at Brackley Hall: Ella and Sam</h3>
    <p class="post-excerpt">Elegant Wedding Of Ella And Sam At Brackley Hall. Relive Their Timeless Celebration. Discover More...</p></div>
    <a class="post-more" href="#">READ MORE</a>
  </article>
</section>

<a class="btn-mark load-more" href="#"><span class="mark"><span></span></span><span class="label">LOAD MORE</span></a>

<footer class="site-footer">
  <div class="footer-rule" style="left:68px"></div>
  <div class="brand">Luke Branwell</div>
  <div class="footer-rule" style="left:755px"></div>
  <nav class="footer-nav">
    <a class="nav-link" href="#" style="left:188px">Home</a>
    <a class="nav-link" href="#" style="left:262px">About Luke</a>
    <a class="nav-link" href="#" style="left:384px">Wedding Films</a>
    <a class="footer-enquire" href="#">ENQUIRE</a>
    <a class="nav-link" href="#" style="left:715px">Blog</a>
    <a class="nav-link" href="#" style="left:782px">Testimonials</a>
    <a class="nav-link" href="#" style="left:900px">Packages</a>
  </nav>
  <div class="footer-divider"></div>
  <p class="copyright">Copyright 2010 - 2024 © Luke Branwell Wedding Films Limited. All Rights Reserved</p>
  <a class="social filled" href="#" aria-label="Social profile" style="left:982px"></a>
  <a class="social" href="#" aria-label="Social profile" style="left:1039px"></a>
  <a class="social" href="#" aria-label="Social profile" style="left:1096px"></a>
</footer>

</body>
</html>
```